Employee Handbook Cover

We need an cover for our employee handbook. The handbook should convey our core values of
-Family
-Accountability
-Professionalism
Attached is our logo. Please visit our website to get a feeling for what we do at www.kelmorvinco.com

```html
<!DOCTYPE html>
<html lang="en">
<head>
<meta charset="utf-8">
<title>Employee Handbook Cover</title>
<link rel="stylesheet" href="https://fonts.googleapis.com/css2?family=Montserrat:wght@500;700;800&family=Tinos:ital@1&display=swap">
<style>
  :root {
    --navy: #2b3990;
    --orange: #f0a35e;
    --steel-light: #f4f5f6;
    --steel-mid: #9aa5ae;
    --steel-dark: #3f4850;
  }
  html, body {
    margin: 0;
    padding: 0;
    overflow: hidden;
  }
  .cover {
    position: relative;
    width: 927px;
    height: 1200px;
    overflow: hidden;
    background: var(--steel-light);
    font-family: "Montserrat", Arial, sans-serif;
  }
  .cover-photo {
    position: absolute;
    inset: 0;
    background:
      radial-gradient(ellipse 190px 230px at 560px 640px, rgba(40,48,56,0.85) 0%, rgba(40,48,56,0.45) 55%, rgba(40,48,56,0) 100%),
      radial-gradient(ellipse 120px 190px at 720px 560px, rgba(50,58,66,0.7) 0%, rgba(50,58,66,0) 100%),
      radial-gradient(ellipse 200px 150px at 260px 520px, rgba(70,80,90,0.7) 0%, rgba(70,80,90,0) 100%),
      radial-gradient(ellipse 260px 110px at 260px 740px, rgba(60,70,80,0.75) 0%, rgba(60,70,80,0) 100%),
      radial-gradient(ellipse 160px 120px at 470px 900px, rgba(35,42,50,0.8) 0%, rgba(35,42,50,0) 100%),
      radial-gradient(ellipse 90px 70px at 330px 700px, rgba(230,234,238,0.6) 0%, rgba(230,234,238,0) 100%),
      radial-gradient(ellipse 80px 60px at 800px 500px, rgba(225,230,235,0.55) 0%, rgba(225,230,235,0) 100%),
      radial-gradient(ellipse 520px 700px at 900px 500px, #8f9aa4 0%, rgba(143,154,164,0) 100%),
      linear-gradient(115deg, #fbfbfb 0%, #eef0f1 28%, #c2c9cf 55%, #9aa5ae 80%, #a9b2ba 100%);
  }
  .title {
    position: absolute;
    left: 0;
    width: 927px;
    text-align: center;
    color: var(--navy);
    margin: 0;
  }
  .title-main {
    top: 100px;
    font-size: 118px;
    font-weight: 700;
    letter-spacing: 6px;
    text-indent: 6px;
    line-height: 1;
    text-shadow: 2px 3px 4px rgba(0,0,0,0.25);
  }
  .title-rule {
    position: absolute;
    top: 214px;
    left: 140px;
    width: 654px;
    height: 8px;
  }
  .title-sub {
    top: 238px;
    font-size: 78px;
    font-weight: 500;
    letter-spacing: 19px;
    text-indent: 19px;
    line-height: 1;
    text-shadow: 2px 3px 4px rgba(0,0,0,0.2);
  }
  .wave {
    position: absolute;
    inset: 0;
  }
  .brand {
    position: absolute;
    top: 1018px;
    left: 0;
    width: 927px;
    display: flex;
    justify-content: center;
    align-items: center;
    gap: 10px;
  }
  .brand-dot {
    width: 68px;
    height: 68px;
    border-radius: 50%;
    background: var(--navy);
  }
  .brand-name {
    font-size: 60px;
    font-weight: 800;
    color: var(--navy);
    line-height: 1;
  }
  .tagline {
    position: absolute;
    top: 1124px;
    left: 30px;
    width: 867px;
    margin: 0;
    text-align: center;
    font-family: "Tinos", "Times New Roman", serif;
    font-style: italic;
    font-size: 16.3px;
    line-height: 22px;
    color: var(--navy);
  }
</style>
</head>
<body>
<div class="cover">
  <div class="cover-photo" role="img" aria-label="Close-up photograph of polished steel transmission gears and shafts on a brushed metal background"></div>

  <h1 class="title title-main">Employee</h1>
  <svg class="title-rule" viewBox="0 0 654 8" aria-hidden="true">
    <rect x="0" y="2" width="212" height="5" fill="var(--orange)"/>
    <rect x="242" y="2" width="188" height="5" fill="var(--orange)"/>
    <rect x="460" y="2" width="194" height="5" fill="var(--orange)"/>
  </svg>
  <h2 class="title title-sub">HANDBOOK</h2>

  <svg class="wave" width="927" height="1200" viewBox="0 0 927 1200" aria-hidden="true">
    <path d="M0,696 C180,860 420,966 600,964 C720,963 840,936 927,912 L927,1200 L0,1200 Z" fill="var(--orange)"/>
  </svg>

  <div class="brand">
    <span class="brand-dot"></span>
    <span class="brand-name">Kelmorvin</span>
  </div>

  <p class="tagline">At Kelmorvin International Corp. we are committed to being the most reliable U.S. source for supplies and parts needed<br>by manufacturers and industrial companies in Mexico and Latin America.</p>
</div>
</body>
</html>
```